Front book cover for a training course to help bakers get higher prices and Tiered Up Profit Plan.

We need a front cover for a book that will be teaching bakers how to sell wedding cakes to get higher prices and book more orders. It is a business book. Do not make it look like we want brides to read it. Bakers will be judging the cover to see if it is worth their investment to read it. The title is already in the logo, so do not repeat it.

Target Market(s)

Bakers who sell wedding cakes

Industry/Entity Type

Bakery

Colors

Designer to choose colors to be used in the design.

Requirements
Must have
• Must use the logo. Must have author name: Lars Finch. Must have subtitle: Boost Your Prices. Book More Brides. Build Your Empire.
Nice to have
• You are free to be creative. The concept is not to be pretty. It is a business sales and marketing book

```html
<!DOCTYPE html>
<html lang="en">
<head>
<meta charset="utf-8">
<title>Tiered Up Profit Plan — Lars Finch</title>
<link rel="stylesheet" href="https://fonts.googleapis.com/css2?family=Bebas+Neue&family=Montserrat:wght@500;600&display=swap">
<style>
  :root {
    --backdrop: #222222;
    --paper: #ffffff;
    --rose: #ef5379;
    --slate: #58585b;
    --ink: #111111;
  }
  html, body {
    margin: 0;
    padding: 0;
    width: 1200px;
    height: 1200px;
    overflow: hidden;
    background: var(--backdrop);
  }
  .cover {
    position: absolute;
    left: 221px;
    top: 31px;
    width: 758px;
    height: 1138px;
    background: var(--paper);
    overflow: hidden;
  }
  .brand-dot {
    position: absolute;
    left: 324px;
    top: 85px;
    width: 110px;
    height: 110px;
    border-radius: 50%;
    background: var(--rose);
  }
  .wordmark {
    position: absolute;
    left: 78px;
    top: 334px;
    width: 604px;
    height: 578px;
    overflow: visible;
  }
  .wordmark text {
    font-family: "Bebas Neue", "Oswald", sans-serif;
    fill: var(--slate);
  }
  .subtitle {
    position: absolute;
    left: 87px;
    top: 933px;
    width: 584px;
    height: 81px;
    border-top: 1.5px solid var(--rose);
    border-bottom: 1.5px solid var(--rose);
    box-sizing: border-box;
    display: flex;
    flex-direction: column;
    justify-content: center;
    align-items: center;
    font-family: "Montserrat", "Helvetica Neue", sans-serif;
    font-weight: 500;
    font-size: 29px;
    line-height: 36px;
    color: var(--ink);
    text-align: center;
    margin: 0;
  }
  .author-band {
    position: absolute;
    left: 0;
    bottom: 0;
    width: 100%;
    height: 90px;
    background: var(--rose);
    display: flex;
    align-items: center;
    justify-content: center;
  }
  .author-name {
    font-family: "Montserrat", "Helvetica Neue", sans-serif;
    font-weight: 600;
    font-size: 50px;
    letter-spacing: 1px;
    color: var(--paper);
    margin: 0;
    text-transform: uppercase;
  }
</style>
</head>
<body>
  <main class="cover">
    <div class="brand-dot" aria-hidden="true"></div>
    <svg class="wordmark" viewBox="0 0 604 578" role="img" aria-label="Tiered Up Profit Plan">
      <text x="0" y="146" font-size="209" textLength="604" lengthAdjust="spacingAndGlyphs">TIERED UP</text>
      <text x="0" y="330" font-size="247" textLength="604" lengthAdjust="spacingAndGlyphs">PROFIT</text>
      <text x="0" y="578" font-size="347" textLength="604" lengthAdjust="spacingAndGlyphs">PLAN</text>
    </svg>
    <p class="subtitle">
      <span>Boost Your Prices. Book More Brides.</span>
      <span>Build Your Empire.</span>
    </p>
    <footer class="author-band">
      <p class="author-name">Lars Finch</p>
    </footer>
  </main>
</body>
</html>
```